Business Card Design

I'm a Naturopathic Physician specializing in the treatment of autoimmune disorders, supportive cancer care and stress, anxiety and depressive disorders.

I practice out of 3 clinic locations and I want a business card design which can be easily changed to include 3 clinic locations, addresses, and contact info.

My website is VelarixND.com and this will promote me personally as a specialist in these treatment areas. I would like one side of the business card to promote this site with the tag line "Specializing in Immune and Related Disorders"

REVIEW THE DESCRIPTION AND UPLOADS FOR MY DESIGN STYLE PREFERENCES.

Industry/Entity Type

Clinic

Colors
9bcb3c
fbed22
0455a3

Requirements
Must have
• Would prefer a vertical design.
Would like bold, simple colors and contrasts

Please visit http://pelquo.com/velarixnd/ for some color and design "feel"

Do not feel the Designs HAVE to have the logo in it... I want SIMPLE, CLEAN and BOLD design so if the Logo makes the designs too busy, please omit

Dr. Gavin Thistlebury BSc ND
Naturopathic Physician

"Clinic Name"
"Clinic Address"
"Clinic Tel"
"Clinic E-Mail"
"Clinic Website"

Please review the PDF for design styles I prefer.

Please Note: Once I determine if there are design concepts worthy of going forward with, I will forward specific contact and clinic information at that time for final design

```html
<!DOCTYPE html>
<html lang="en">
<head>
<meta charset="utf-8">
<title>VelarixND Business Card</title>
<link rel="stylesheet" href="https://fonts.googleapis.com/css2?family=Open+Sans:wght@400;600;700&display=swap">
<style>
  :root {
    --navy: #064a72;
    --navy-deep: #033a5c;
    --ink: #0b4a86;
    --green: #9bcb3c;
    --lime: #c3dc2e;
    --yellow: #fbed22;
    --paper: #ffffff;
    --backdrop: #ecebe8;
  }
  * { box-sizing: border-box; margin: 0; padding: 0; }
  html, body { width: 1108px; height: 1200px; overflow: hidden; }
  body {
    background: var(--backdrop);
    font-family: "Open Sans", Arial, sans-serif;
    position: relative;
  }
  .card {
    position: absolute;
    top: 180px;
    width: 490px;
    height: 840px;
    overflow: hidden;
    box-shadow: 0 6px 18px rgba(0,0,0,0.18);
  }
  .card--back {
    left: 44px;
    background: radial-gradient(ellipse at 45% 35%, #0b5a86 0%, var(--navy) 45%, var(--navy-deep) 100%);
    color: var(--paper);
  }
  .card--front { left: 574px; background: var(--paper); color: var(--ink); }

  .brand {
    font-weight: 700;
    font-size: 58px;
    letter-spacing: 0.5px;
    line-height: 1;
    text-align: center;
  }
  .card--back .brand { position: absolute; top: 250px; left: 0; right: 0; color: var(--paper); }
  .card--front .brand { position: absolute; top: 80px; left: 0; right: 0; color: var(--ink); }

  .tagline {
    font-size: 27px;
    line-height: 1.2;
    text-align: center;
    position: absolute;
    left: 0; right: 0;
  }
  .card--back .tagline { top: 340px; }
  .card--front .tagline { top: 160px; }

  .web-footer {
    position: absolute;
    bottom: 95px; left: 0; right: 0;
    text-align: center;
    font-size: 26px;
    letter-spacing: 0.5px;
  }

  .field {
    position: absolute;
    left: 0; top: 290px;
    width: 490px; height: 550px;
  }
  .field-glow {
    position: absolute;
    left: 0; top: 40px; right: 0; bottom: 0;
    background:
      radial-gradient(circle at 75% 20%, rgba(251,237,34,0.35) 0, rgba(251,237,34,0) 40%),
      radial-gradient(circle at 20% 85%, rgba(251,237,34,0.3) 0, rgba(251,237,34,0) 45%),
      linear-gradient(160deg, var(--green) 0%, var(--lime) 55%, #b6d534 100%);
  }
  .field svg { position: absolute; left: 0; top: 0; }

  .doctor {
    position: absolute;
    left: 40px; top: 495px;
    font-weight: 600;
    font-size: 28px;
    color: var(--ink);
  }
  .role {
    position: absolute;
    left: 40px; top: 545px;
    font-size: 22px;
    color: var(--ink);
  }
  .contacts {
    position: absolute;
    left: 36px; top: 620px;
    list-style: none;
    font-size: 22px;
    color: var(--ink);
  }
  .contacts li { display: flex; align-items: flex-start; gap: 14px; line-height: 29px; }
  .contacts svg { flex: none; margin-top: 4px; }
  .contacts .address { margin-top: 4px; line-height: 24px; }
</style>
</head>
<body>

<section class="card card--back">
  <div class="brand">VelarixND</div>
  <p class="tagline">Specializing in Immune<br>and Related Disorders</p>
  <p class="web-footer">www.velarixnd.com</p>
</section>

<section class="card card--front">
  <div class="brand">VelarixND</div>
  <p class="tagline">Specializing in Immune<br>and Related Disorders</p>

  <div class="field">
    <div class="field-glow"></div>
    <svg width="490" height="110" viewBox="0 0 490 110">
      <path d="M0 0 C90 40 180 60 270 30 C350 5 420 -5 490 20 L490 40 C420 20 350 25 280 55 C190 90 90 70 0 30 Z" fill="var(--navy)"/>
      <path d="M0 30 C90 70 190 90 280 55 C350 25 420 20 490 40 L490 110 L0 110 Z" fill="var(--green)" opacity="0"/>
    </svg>
  </div>

  <h1 class="doctor">Dr. Gavin Thistlebury BSc ND</h1>
  <p class="role">Naturopathic Physician</p>

  <ul class="contacts">
    <li>
      <svg width="20" height="20" viewBox="0 0 20 20" aria-hidden="true"><circle cx="10" cy="10" r="10" fill="var(--ink)"/><path d="M5 8 Q10 4 15 8 L14 10 L12 9 L12 8 L8 8 L8 9 L6 10 Z M6 11 H14 V14 H6 Z" fill="#fff"/></svg>
      <span>04.517.2290</span>
    </li>
    <li>
      <svg width="20" height="20" viewBox="0 0 20 20" aria-hidden="true"><circle cx="10" cy="10" r="10" fill="var(--ink)"/><rect x="5" y="6.5" width="10" height="7" fill="#fff"/><path d="M5 6.5 L10 11 L15 6.5" fill="none" stroke="var(--ink)" stroke-width="1.2"/></svg>
      <span>email@address.com</span>
    </li>
    <li>
      <svg width="20" height="20" viewBox="0 0 20 20" aria-hidden="true"><circle cx="10" cy="10" r="10" fill="var(--ink)"/><g fill="none" stroke="#fff" stroke-width="1.1"><circle cx="10" cy="10" r="5.5"/><ellipse cx="10" cy="10" rx="2.4" ry="5.5"/><path d="M4.5 10 H15.5"/></g></svg>
      <span>www.velarixnd.com</span>
    </li>
    <li>
      <svg width="20" height="22" viewBox="0 0 20 22" aria-hidden="true"><path d="M10 0 A9 9 0 0 1 19 9 C19 15 10 22 10 22 C10 22 1 15 1 9 A9 9 0 0 1 10 0 Z" fill="var(--ink)"/><circle cx="10" cy="9" r="3.2" fill="#fff"/></svg>
      <span class="address">Clinic Name Here<br>PO Box 1234 St<br>Your Address Text<br>City Here 5678</span>
    </li>
  </ul>
</section>

</body>
</html>
```